Surgical Sales Presentation Folder

Presentation folder; three panel; custom cutouts; Six 8.5 x 11 full color sales sheets to be bound into presentation folder; 5 full color sales sheets, stepped, longest being 8.5 x 11.
We are Kelvar Surgical Group and we are a surgical company that supports physicians who wish to become surgeons. Our clients are Physicians. As such, the design needs to be very professional.
I have included a list of photos and a letter describing what we like about each photo. I have included the verbiage with page identifiers. If this makes scene, please feel free to add photos to the inside of the folder or I can provide you with examples that we think are similar to what we are looking for.
Updates
Target Market(s)
Doctors who want to be surgeons.
Industry/Entity Type
Sales
Requirements
Must have
- Presentation folder; three panel; custom cutouts; Six 8.5 x 11 full color sales sheets to be bound into presentation folder; 5 full color sales sheets, stepped, longest being 8.5 x 11.

```html
<!DOCTYPE html>
<html lang="en">
<head>
<meta charset="utf-8">
<title>Medical Practice vs. Surgical Practice – Kelvar Surgical Group</title>
<link href="https://fonts.googleapis.com/css2?family=Arimo:wght@400;700&display=swap" rel="stylesheet">
<style>
  :root {
    --title-blue: #1d8fd1;
    --body-ink: #1c1c1c;
    --page: #ffffff;
    --edge: #d9dadb;
    --footer-dark: #0b0b0c;
    --footer-mid: #2a2b2d;
    --brand-blue: #2f8fd6;
    --photo-light: #d8e6f2;
    --photo-mid: #7ea7c8;
    --photo-dark: #2e5573;
    --emblem-light: #bfe0f4;
    --emblem-mid: #4aa3d8;
  }
  * { margin: 0; padding: 0; box-sizing: border-box; }
  html, body { width: 927px; height: 1200px; overflow: hidden; background: var(--page); }
  .sheet {
    position: relative;
    width: 927px;
    height: 1200px;
    background: var(--page);
    border: 3px solid var(--edge);
    border-bottom: none;
    font-family: "Arimo", Arial, sans-serif;
    color: var(--body-ink);
    overflow: hidden;
  }
  .sheet-title {
    position: absolute;
    left: 44px;
    top: 86px;
    font-family: "Arimo", Arial, sans-serif;
    font-weight: 700;
    font-size: 35.5px;
    line-height: 40px;
    color: var(--title-blue);
  }
  .emblem {
    position: absolute;
    left: 742px;
    top: 36px;
    width: 138px;
    height: 146px;
    border-radius: 40px 40px 10px 10px;
    background: radial-gradient(ellipse at 50% 35%, var(--emblem-light), var(--emblem-mid) 75%, rgba(74,163,216,0.15));
    opacity: 0.55;
  }
  .copy { position: absolute; font-size: 18.5px; line-height: 23px; }
  .copy p + p, .copy p + ul, .copy ul + p { margin-top: 22px; }
  .copy ul { list-style: none; }
  .copy li { position: relative; padding-left: 10px; margin-top: 4px; }
  .copy li::before {
    content: "";
    position: absolute;
    left: -15px;
    top: 8px;
    width: 7px;
    height: 7px;
    border-radius: 50%;
    background: var(--body-ink);
  }
  .copy ul ul { margin-top: 1px; padding-left: 18px; }
  .copy ul ul li { margin-top: 1px; }
  .survey-block { left: 67px; top: 200px; width: 760px; }
  .surgeon-block { left: 67px; top: 528px; width: 362px; }
  .instrument-photo {
    position: absolute;
    left: 448px;
    top: 516px;
    width: 452px;
    height: 488px;
    background: linear-gradient(160deg, var(--photo-light) 0%, var(--photo-mid) 45%, var(--photo-dark) 100%);
  }
  .footer-band {
    position: absolute;
    left: 0;
    bottom: 0;
    width: 100%;
    height: 118px;
    background: linear-gradient(180deg, var(--footer-mid) 0%, var(--footer-dark) 55%, var(--footer-dark) 100%);
    border-top: 2px solid #9a9b9d;
  }
  .brand {
    position: absolute;
    left: 40px;
    top: 28px;
    display: flex;
    align-items: center;
    gap: 14px;
  }
  .brand-dot {
    width: 54px;
    height: 54px;
    border-radius: 50%;
    background: var(--brand-blue);
  }
  .brand-name {
    font-family: "Arimo", Arial, sans-serif;
    font-weight: 700;
    font-size: 30px;
    color: var(--brand-blue);
    letter-spacing: 0.5px;
  }
</style>
</head>
<body>
<main class="sheet">
  <h1 class="sheet-title">Medical Practice vs. Surgical Practice</h1>
  <div class="emblem" role="img" aria-label="Blue medical caduceus emblem"></div>

  <section class="copy survey-block">
    <p>Clinicore/Health Daily conducted a survey of 24,000 physicians representing 25 different medical specialties. They found that:</p>
    <ul>
      <li>Only 54% of the physicians said they would choose medicine again as a career, down from 69% only three years ago.</li>
      <li>Just 41% would choose the same specialty again.</li>
      <li>Only 25% of doctors said they would choose the same practice setting, compared with 50% two years ago.</li>
      <li>This same article identifies, “frustration and discontent among physicians” due to:
        <ul>
          <li>Declining incomes</li>
          <li>Excessive paperwork</li>
          <li>Vast uncertainty about changes dictated by the Affordable Care Act</li>
        </ul>
      </li>
    </ul>
  </section>

  <section class="copy surgeon-block">
    <p>When we look specifically at surgeons, the Journal of Surgical Practice found that with respect to career satisfaction:</p>
    <ul>
      <li>71 % of the study participants indicated that they would become a physician again.</li>
      <li>74% would become a surgeon again, if they could revisit their specialty choice.</li>
      <li>And they included Plastic Surgeons in the specialties with the greatest satisfaction with overall career choice.</li>
    </ul>
    <p>In fact, according to an article in Market Wire News, the highest paying profession last year was Surgery!</p>
  </section>

  <div class="instrument-photo" role="img" aria-label="Blue-toned photograph of surgical instruments: forceps, scissors and a steel bowl on a cloth"></div>

  <footer class="footer-band">
    <div class="brand">
      <span class="brand-dot"></span>
      <span class="brand-name">Kelvar Surgical Group</span>
    </div>
  </footer>
</main>
</body>
</html>
```